VORdyne stands for Valve & Output Regulation dynamics and specialises in process automation

We are a New company called VORdyne (Valve & Output Regulation dynamics) a Brisbane based company speciallising in Process Automation for the oil and Gas industry in Australia. We work on projects for DCS, RTU and PLC automation this involves programming and commissioning. We initially need a Website that customers can see about the company and make enquiries. We currently have Royal Blue and grey as our colours on our email signatures but are open for suggestions. Keywords i would suggest yo to look at for insperation are CSG ( coalseam gas) DCS (Distributed control system) RTU (remote terminal unit) and PLC (programmable logic controller).

Target Market(s)

Large CSG companies in Australia, Tellory, Brenmark, HJV, Fenwy

Industry/Entity Type

Industry

```html
<!DOCTYPE html>
<html lang="en">
<head>
<meta charset="utf-8">
<title>VORdyne – Process Automation</title>
<link rel="stylesheet" href="https://fonts.googleapis.com/css2?family=Squada+One&family=Teko:wght@600&family=Oswald:wght@300&family=Arimo:wght@400;700&display=swap">
<style>
:root{
  --royal:#1b2a85;
  --grey-bg:#eeeeee;
  --footer-bg:#ececec;
  --card:#4a4a4a;
  --card-edge:#5c5c5c;
  --text:#333333;
  --muted:#777777;
  --white:#ffffff;
  --field:#d9d9d9;
}
*{box-sizing:border-box;margin:0;padding:0}
html,body{width:766px;height:1200px;overflow:hidden;background:var(--white)}
body{font-family:"Arimo",Arial,sans-serif;color:var(--text);position:relative}
.page{position:relative;width:766px;height:1200px;overflow:hidden}
.abs{position:absolute}

/* header */
.brand{left:14px;top:16px;display:flex;align-items:center;gap:6px}
.brand-square{width:11px;height:11px;background:var(--royal)}
.brand-name{font-weight:700;font-size:30px;color:var(--royal);letter-spacing:-0.5px;line-height:1}
.tagline{left:30px;top:52px;font-size:8px;color:#555}
.top-links{right:10px;top:53px;font-size:8px;color:#222}

/* nav */
.nav{left:0;top:77px;width:766px;height:29px;background:var(--royal)}
.nav a{position:absolute;top:0;line-height:29px;font-family:"Squada One",sans-serif;color:var(--white);text-decoration:none;font-size:12px;letter-spacing:.3px;white-space:nowrap}

.hero{left:0;top:106px;width:766px;height:279px;background:linear-gradient(100deg,#6f6a62 0%,#b7b0a2 35%,#8a8377 60%,#c7c3ba 80%,#5d5d60 100%)}

/* products */
.products{left:0;top:385px;width:766px;height:321px;background:var(--grey-bg)}
.heading{font-family:"Teko",sans-serif;font-weight:600;line-height:1;letter-spacing:.5px}
.products-title{left:10px;top:399px;font-size:34px;color:#222}
.card{width:242px;height:245px;top:437px;background:var(--card);border:1px solid var(--card-edge)}
.card-photo{position:absolute;left:6px;top:6px;width:230px;height:138px}
.card-label{position:absolute;left:0;top:149px;height:24px;background:var(--royal);color:var(--white);font-family:"Oswald",sans-serif;font-weight:300;font-size:14.5px;line-height:24px;padding:0 15px;letter-spacing:-.2px;white-space:nowrap}
.card-text{position:absolute;left:18px;top:179px;width:215px;font-size:8.6px;line-height:11.5px;color:#e6e6e6}
.card-btn{position:absolute;left:18px;top:219px;width:59px;height:16px;background:#f0f0f0;border:1px solid #bbb;font-size:8px;font-weight:700;color:#222;text-align:center;line-height:14px}

/* info */
.section-title{font-size:36px;color:var(--royal)}
.testimonial{left:17px;width:292px;font-size:8.6px;line-height:11.5px;color:#333}
.testimonial-by{left:17px;font-size:8.8px;font-weight:700;color:var(--royal)}
.divider{left:17px;top:854px;width:287px;height:1px;background:#bbb}
.bullets{list-style:none;font-size:8.9px;color:#444}
.bullets li{height:15.7px;display:flex;align-items:center}
.bullets li::before{content:"";width:4px;height:4px;border:1.5px solid #444;border-radius:50%;margin-right:7px}

/* footer */
.footer{left:0;top:985px;width:766px;height:215px;background:var(--footer-bg)}
.footer-title{font-size:25px;color:#555}
.foot-links{font-size:8.8px;line-height:11.4px;color:var(--muted)}
.field{left:262px;width:200px;background:var(--field);border:1px solid #c6c6c6;border-radius:4px;font-size:8.8px;font-weight:700;color:#444;padding:4px 10px}
.send{left:400px;top:1162px;width:60px;height:18px;background:#9a9a9a;border:1px solid #bcbcbc;color:var(--white);font-size:8.5px;font-weight:700;text-align:center;line-height:16px}
.contact{left:542px;top:1050px;font-size:8.8px;line-height:11.4px;color:#333;font-style:normal}
.social{left:541px;top:1103px;display:flex;gap:8px}
.social span{width:21px;height:21px;border-radius:50%;background:#a9a9a9}
</style>
</head>
<body>
<div class="page">
  <header>
    <div class="abs brand"><span class="brand-square"></span><span class="brand-name">VORdyne</span></div>
    <div class="abs tagline">Valve &amp; Output Regulation dynamics</div>
    <div class="abs top-links">home · sitemap · careers · contact</div>
  </header>

  <nav class="abs nav">
    <a href="#" style="left:17px">HOME</a>
    <a href="#" style="left:68px">ABOUT</a>
    <a href="#" style="left:121px">SERVICES</a>
    <a href="#" style="left:186px">SOLUTIONS</a>
    <a href="#" style="left:258px">CLIENTS</a>
    <a href="#" style="left:318px">EXPERIENCES</a>
    <a href="#" style="left:400px">LATEST NEWS</a>
    <a href="#" style="left:486px">CONTACT US</a>
  </nav>

  <div class="abs hero" role="img" aria-label="Industrial production line with stainless steel machinery"></div>

  <section class="abs products"></section>
  <h2 class="abs heading products-title">MAIN PRODUCTS</h2>

  <article class="abs card" style="left:6px">
    <div class="card-photo" role="img" aria-label="Distributed control system rack with I/O modules" style="background:linear-gradient(180deg,#c9ccd0,#8e9196 70%,#d6d6d6)"></div>
    <div class="card-label">DISTRIBUTED CONTROL SYSTEM</div>
    <p class="card-text">Lorem ipsum dolor sit amet, consectetur adipisicing elit, sed do eiusmod tempor incididunt ut labore et dolore magna aliqua. Ut enim ad minim .</p>
    <div class="card-btn">INQUIRE</div>
  </article>
  <article class="abs card" style="left:263px">
    <div class="card-photo" role="img" aria-label="Remote terminal unit panel with gauges and switches" style="background:linear-gradient(160deg,#8f978a,#c3c8bd 50%,#9aa096)"></div>
    <div class="card-label">REMOTE TERMINAL UNIT</div>
    <p class="card-text">Sed ut perspiciatis, unde omnis iste natus error sit voluptatem accusantium doloremque laudantium, totam rem aperiam eaque ipsa, quae ab illo .</p>
    <div class="card-btn">INQUIRE</div>
  </article>
  <article class="abs card" style="left:516px">
    <div class="card-photo" role="img" aria-label="Control room monitors running PLC software" style="background:linear-gradient(180deg,#e7e9ec,#c4cad6 55%,#eeeeee)"></div>
    <div class="card-label">PROGRAMMABLE LOGIC CONTROLLER</div>
    <p class="card-text">Nemo enim ipsam voluptatem, quia voluptas sit, aspernatur aut odit aut fugit, sed quia consequuntur magni dolores eos, qui ratione voluptatem sequi.</p>
    <div class="card-btn">INQUIRE</div>
  </article>

  <h2 class="abs heading section-title" style="left:16px;top:735px">TESTIMONIALS</h2>
  <p class="abs testimonial" style="top:777px">At vero eos et accusamus et iusto odio dignissimos ducimus, qui blanditiis praesentium voluptatum deleniti atque corrupti, quos dolores et quas molestias excepturi sint, obcaecati cupiditate non provident, similique sunt in culpa, qui officia deserunt mollitia animi, id est</p>
  <div class="abs testimonial-by" style="top:829px">by: oil industry name</div>
  <div class="abs divider"></div>
  <p class="abs testimonial" style="top:870px">Temporibus autem quibusdam et aut officiis debitis aut rerum necessitatibus saepe eveniet, ut et voluptates repudiandae sint et molestiae non recusandae. Itaque earum rerum hic tenetur a sapiente delectus, ut aut reiciendis voluptatibus maiores alias consequatur.</p>
  <div class="abs testimonial-by" style="top:922px">by: another client</div>

  <h2 class="abs heading section-title" style="left:366px;top:735px">SERVICES</h2>
  <ul class="abs bullets" style="left:375px;top:774px">
    <li>Consulting &amp; Design</li><li>Project Management</li><li>Engineering Services</li><li>Solutions</li><li>PLC / PAC / RTU</li><li>SCADA / HMI</li><li>Industrial Networking &amp; IT</li><li>Business Intelligence</li><li>Onsite Services, Support &amp; Training</li>
  </ul>

  <h2 class="abs heading section-title" style="left:578px;top:735px">SOLUTIONS</h2>
  <ul class="abs bullets" style="left:586px;top:774px">
    <li>Mining</li><li>Oil &amp; Gas</li><li>Water</li><li>Food &amp; Beverage</li><li>Manufacturing</li><li>Commercial</li>
  </ul>

  <footer class="abs footer"></footer>
  <h3 class="abs heading footer-title" style="left:18px;top:1015px">NAVIGATION</h3>
  <div class="abs foot-links" style="left:20px;top:1052px">Home<br>About<br>Services<br>Solutions<br>Clients<br>Experiences</div>
  <div class="abs foot-links" style="left:99px;top:1052px">Sitemap<br>Latest News<br>Privacy Policy<br>Terms of Use<br>Contact Us</div>

  <h3 class="abs heading footer-title" style="left:264px;top:1015px">INQUIRE NOW</h3>
  <div class="abs field" style="top:1050px;height:21px">full name</div>
  <div class="abs field" style="top:1073px;height:21px">email</div>
  <div class="abs field" style="top:1095px;height:58px">inquries</div>
  <div class="abs send">INQUIRE</div>

  <h3 class="abs heading footer-title" style="left:541px;top:1015px">CONTACT US</h3>
  <address class="abs contact">Level 2, 48 Harlow Street<br>Kelvin Grove QLD 4059<br>Ph: +61-7-5550 0142 / Fax: +61-7-5550 0143<br>Email: sales@vordyne.com.au</address>
  <div class="abs social" aria-label="Social links"><span></span><span></span><span></span><span></span><span></span></div>
</div>
</body>
</html>
```